NOTE: I PROVIDED THE INCORRECT LOGO AND ONLY A HANDFUL OF PEOPLE NOTICED THAT IT WAS NOT THE ONE I DESCRIBED. THE LOGO I HAVE NOW ATTACHED MATCHES MY WEBSITE AND THE COLORS ON THE WEBSITE SHOULD BE USED FOR THE CARD.

PLEASE READ THE BUSINESS CARD DETAILS AND PROJECT MUST HAVES CAREFULLY.

I am looking for a business card that is powerful, a bit edgy, and although I work in the corporate world, not too formal. I would like to see designs that use the colors on my website www.brightmoorlane.com. I don't want the card to look washed out so please use shades of those colors that make them "pop". The "vibe" of the card needs to show substance and confidence while also reflecting that we're not your usual consultants.

The focus of my work is turning "people problems" into profits. Those problems could be poor service, an unstable workforce, untrained leaders, or managing change. We are an aggressive, results-focused team of performance improvement professionals who refuse to believe "things can't be done". For us, failure is not an option. Our logo reflects a target from the view of the site on a gun.

In addition to the contact information provided on the sample business card (do not include "turning people problems into profits"), I would like to include this statement (probably on the back):
I equip results-oriented business leaders to turn their people problems into profits in six months or less.

PLEASE NOTE THAT MY WEBSITE IS UNDER REVISION TO TONE DOWN THE MILITARY THEME, ALTHOUGH THE WARRIOR ENERGY AND FOCUS ON RESULTS REMAINS.

Target Market(s)

My clients are Mid and senior-level managers. I don't target any particular industry.

Industry/Entity Type

Consulting

Contact Information for Business Card

In addition to the contact information provided on the sample business card (DO NOT INCLUDE "turning people problems into profits"), I would like to include this statement (probably on the back):

I don't care whether the card is landscape or portrait view.

Font styles to use
Sans Serif

Requirements
Must have
• 1. be easy to read, no 6-8 point fonts!
• 2. a "vibe" that captures the eye without being too chaotic or busy
• 3. bold color, not washed out or boring - a good blend with the colors currently on my website (black, red, white, army green) but you don't need to use all of them.
• 4. all the contact information I have provided
• 5. a good blend with the colors currently on my website
• 6. Must have this quote on the back of the card: I equip results-oriented business leaders to turn their people problems into profits in six months or less.
Nice to have
• In looking at the sample images I provided for ideas, you can see that I like the way a card carries over from one side to the next.
• It would be great to find some aspect/quality/feature that I haven't seen before
Should not have
• 1. NO use of ALL CAPS
• 2. fonts that I would have to seek out and purchase (you should provide files for font if using something not standard)

```html
<!DOCTYPE html>
<html lang="en">
<head>
<meta charset="utf-8">
<title>Brightmoor Lane business card</title>
<link rel="stylesheet" href="https://fonts.googleapis.com/css2?family=Montserrat:wght@500;600&family=Roboto+Condensed:wght@700&display=swap">
<style>
  :root {
    --canvas: #e9e6df;
    --card-black: #111112;
    --card-black-hi: #1e1e20;
    --army-green: #3f4a2c;
    --army-green-hi: #4e5a3a;
    --logo-green: #5a6a48;
    --signal-red: #e23a33;
    --white: #f4f4f2;
  }
  * { box-sizing: border-box; margin: 0; padding: 0; }
  html, body { width: 1200px; height: 942px; overflow: hidden; }
  body {
    background: var(--canvas);
    display: flex;
    align-items: center;
    justify-content: center;
    gap: 60px;
  }
  .card {
    position: relative;
    width: 400px;
    height: 680px;
    background: linear-gradient(160deg, var(--card-black-hi), var(--card-black) 55%);
    overflow: hidden;
    box-shadow: 0 14px 30px rgba(0,0,0,.25);
  }
  .brand {
    position: absolute;
    display: flex;
    align-items: center;
    gap: 12px;
    font-family: "Roboto Condensed", sans-serif;
    font-weight: 700;
    color: var(--logo-green);
    line-height: 1;
  }
  .brand-dot {
    width: 58px; height: 58px;
    border-radius: 50%;
    background: var(--logo-green);
    flex: none;
  }
  .brand-name { font-size: 38px; }

  /* Front */
  .card-front .brand { left: 34px; top: 150px; }
  .front-panel {
    position: absolute; inset: 0;
    background: linear-gradient(150deg, var(--army-green-hi), var(--army-green) 60%, #344024);
    clip-path: polygon(0 56%, 100% 49%, 100% 100%, 0 100%);
  }
  .front-wedge {
    position: absolute; inset: 0;
    background: var(--signal-red);
    clip-path: polygon(0 46%, 24% 54.3%, 0 56%);
  }
  .person {
    position: absolute; left: 40px; top: 440px;
    font-family: "Montserrat", sans-serif;
  }
  .person-name { color: var(--white); font-size: 30px; font-weight: 600; }
  .person-title { color: var(--signal-red); font-size: 17px; font-weight: 500; margin-top: 2px; }
  .contact-list {
    list-style: none;
    position: absolute; left: 40px; top: 530px;
    font-family: "Montserrat", sans-serif;
    font-size: 17px; font-weight: 500;
    color: var(--white);
  }
  .contact-item { display: flex; align-items: center; gap: 14px; height: 31px; }
  .contact-icon { width: 20px; height: 20px; flex: none; }

  /* Back */
  .back-bar { position: absolute; background: var(--signal-red); }
  .back-bar-left { left: 0; top: 370px; width: 52px; height: 110px; }
  .back-bar-right { right: 0; top: 150px; width: 40px; height: 115px; }
  .card-back .brand { left: 70px; top: 255px; }
  .statement {
    position: absolute; left: 40px; right: 40px; top: 520px;
    text-align: center;
    font-family: "Roboto Condensed", sans-serif;
    font-weight: 700;
    font-size: 19px;
    line-height: 1.3;
    color: var(--logo-green);
  }
</style>
</head>
<body>
  <section class="card card-front" aria-label="Card front">
    <div class="front-panel"></div>
    <div class="front-wedge"></div>
    <div class="brand">
      <span class="brand-dot"></span>
      <span class="brand-name">Brightmoor<br>Lane</span>
    </div>
    <div class="person">
      <p class="person-name">Dana Whitfield</p>
      <p class="person-title">Chief Performance Strategist</p>
    </div>
    <ul class="contact-list">
      <li class="contact-item">
        <svg class="contact-icon" viewBox="0 0 20 20" fill="none" stroke="var(--signal-red)" stroke-width="1.8"><rect x="5" y="1.5" width="10" height="17" rx="1.5"/><line x1="9" y1="15.5" x2="11" y2="15.5"/></svg>
        <span>555-014-2286</span>
      </li>
      <li class="contact-item">
        <svg class="contact-icon" viewBox="0 0 20 20"><rect x="1" y="4" width="18" height="12" fill="var(--signal-red)"/><polyline points="1,4 10,11 19,4" fill="none" stroke="var(--army-green)" stroke-width="1.6"/></svg>
        <span>dana@brightmoorlane.com</span>
      </li>
      <li class="contact-item">
        <svg class="contact-icon" viewBox="0 0 20 20" fill="var(--signal-red)"><path d="M2 6c0-2 2-3 8-3s8 1 8 3v2h-4V6.5H6V8H2z"/><rect x="3" y="9" width="14" height="8" rx="1.5"/></svg>
        <span>555-014-7730</span>
      </li>
      <li class="contact-item">
        <svg class="contact-icon" viewBox="0 0 20 20" fill="none" stroke="var(--signal-red)" stroke-width="1.5"><circle cx="10" cy="10" r="8"/><ellipse cx="10" cy="10" rx="3.5" ry="8"/><line x1="2" y1="10" x2="18" y2="10"/></svg>
        <span>www.brightmoorlane.com</span>
      </li>
    </ul>
  </section>

  <section class="card card-back" aria-label="Card back">
    <div class="back-bar back-bar-right"></div>
    <div class="back-bar back-bar-left"></div>
    <div class="brand">
      <span class="brand-dot"></span>
      <span class="brand-name">Brightmoor<br>Lane</span>
    </div>
    <p class="statement">I equip results-oriented business leaders to turn their people problems into profits in six months or less.</p>
  </section>
</body>
</html>
```